Business card for law firm

Need business card for new law firm. Think confident, authoritative, conservative, but not stuffy or old-fashioned.

Contact Information for Business Card

Content for card - logo (uploaded), plus the following:

Paul Wexbury (larger font)
Managing Partner (larger font, but not as large as name)
Level 9, 41 Tansy Lane
Sydney NSW 2000
Main Tel 02 7346 2190
Direct Tel 02 6273 4415
Email paul@qvlegal.com.au
www.qvlegal.com.au

Letterhead design should include logo plus:
Level 9, 41 Tansy Lane
Sydney NSW 2000
Tel 02 6273 4415
www.qvlegal.com.au

```html
<!DOCTYPE html>
<html lang="en">
<head>
<meta charset="utf-8">
<title>Quillvale Lawyers — Business Card</title>
<link rel="stylesheet" href="https://fonts.googleapis.com/css2?family=Cardo:wght@400;700&display=swap">
<style>
  :root {
    --navy: #1f2758;
    --ink: #141414;
    --paper: #f2f3f5;
    --paper-light: #fbfbfc;
    --paper-shade: #dcdde1;
    --white: #ffffff;
  }
  * { margin: 0; padding: 0; box-sizing: border-box; }
  html, body {
    width: 707px;
    height: 1200px;
    overflow: hidden;
    background: var(--paper);
  }
  .card {
    position: relative;
    width: 707px;
    height: 1200px;
    overflow: hidden;
    font-family: "Cardo", Georgia, serif;
    color: var(--ink);
    text-align: center;
  }
  .card__backdrop {
    position: absolute;
    inset: 0;
    background:
      linear-gradient(135deg, rgba(255,255,255,0) 20%, rgba(255,255,255,0.75) 32%, rgba(255,255,255,0) 44%),
      linear-gradient(45deg, rgba(210,212,218,0.55) 0%, rgba(255,255,255,0) 30%, rgba(220,222,228,0.45) 55%, rgba(255,255,255,0) 75%),
      linear-gradient(180deg, var(--paper-shade) 0%, var(--paper) 35%, var(--paper-light) 80%, var(--white) 100%);
  }
  .brand {
    position: absolute;
    top: 100px;
    left: 0;
    width: 100%;
  }
  .brand__mark {
    display: block;
    width: 96px;
    height: 96px;
    margin: 0 auto;
    background: var(--navy);
  }
  .brand__name {
    margin-top: 56px;
    color: var(--ink);
    font-weight: 400;
  }
  .brand__firm {
    display: block;
    font-size: 54px;
    line-height: 1;
    letter-spacing: 0.06em;
    padding-left: 0.06em;
  }
  .brand__type {
    display: block;
    margin-top: 16px;
    font-size: 20px;
    line-height: 1;
    letter-spacing: 0.95em;
    padding-left: 0.95em;
  }
  .person__name {
    position: absolute;
    top: 534px;
    left: 0;
    width: 100%;
    font-size: 58px;
    font-weight: 400;
    line-height: 1;
  }
  .person__role {
    position: absolute;
    top: 612px;
    left: 90px;
    width: 555px;
    height: 58px;
  }
  .person__role svg { position: absolute; inset: 0; }
  .person__role-text {
    position: relative;
    display: block;
    line-height: 58px;
    font-size: 28px;
    color: var(--white);
    letter-spacing: 0.03em;
  }
  .contact {
    position: absolute;
    top: 793px;
    left: 0;
    width: 100%;
    font-size: 29px;
    line-height: 1.12;
  }
  .contact__phones {
    margin-top: 10px;
    font-weight: 700;
    font-size: 30px;
    line-height: 1.25;
  }
  .contact__online { margin-top: 10px; line-height: 1.5; }
  .card__band {
    position: absolute;
    left: 0;
    bottom: 0;
    width: 100%;
    height: 51px;
    background: var(--navy);
  }
</style>
</head>
<body>
  <div class="card">
    <div class="card__backdrop" role="img" aria-label="Soft grey background with faint diagonal light streaks"></div>

    <header class="brand">
      <span class="brand__mark"></span>
      <h1 class="brand__name">
        <span class="brand__firm">QUILLVALE</span>
        <span class="brand__type">LAWYERS</span>
      </h1>
    </header>

    <h2 class="person__name">Paul Wexbury</h2>

    <div class="person__role">
      <svg width="555" height="58" viewBox="0 0 555 58" aria-hidden="true">
        <polygon points="0,0 555,0 530,29 555,58 0,58 25,29" fill="var(--navy)"/>
      </svg>
      <span class="person__role-text">•••• MANAGING PARTNER ••••</span>
    </div>

    <address class="contact" style="font-style: normal;">
      <p class="contact__address">Level 9, 41 Tansy Lane<br>Sydney NSW 2000</p>
      <p class="contact__phones">Main Tel 02 7346 2190<br>Direct Tel 02 6273 4415</p>
      <p class="contact__online">Email paul@qvlegal.com.au<br>Website www.qvlegal.com.au</p>
    </address>

    <div class="card__band"></div>
  </div>
</body>
</html>
```